Quarry Lane Co. needs Business Cards

For this project, we need business cards (currently have also put a call out for a logo). We are a start-up called Quarry Lane Co. This is our second company (our first one was called Brightwickery). Traditionally we have been providing market research services across different sectors, primarily financial services and the pharmaceutical industry. However, we now want to go beyond market research to offer more (Etc.)... strategic consulting and big data knowledge management. We want our brand to be approachable, creative, fun but professional.

Target Market(s)

The target audience is a business professional - we are B2B (business to business) and do not sell our services to individuals. The brands we work with are major brands across industries, but primarily automotive, financial and pharmaceutical.

Industry/Entity Type

Market Research

Font styles to use
Serif
Sans Serif
Other font styles liked:
• Calibri

Requirements
Must have
• Be clean, simple, modern
Show our address and phone number and email address and website URL
We do not need to have titles showing.

```html
<!DOCTYPE html>
<html lang="en">
<head>
<meta charset="utf-8">
<title>Quarry Lane Co. — Business Card</title>
<link rel="stylesheet" href="https://fonts.googleapis.com/css2?family=Arimo:wght@400&family=Tinos:wght@700&display=swap">
<style>
  :root {
    --page-bg: #ececec;
    --card-bg: #ffffff;
    --brand-red: #7d1416;
    --accent-red: #8f1a1c;
    --ink: #1f1f1f;
    --photo-dark: #2a2422;
    --photo-warm: #b5824f;
  }
  html, body {
    margin: 0;
    width: 1200px;
    height: 864px;
    overflow: hidden;
    background: var(--page-bg);
  }
  .card {
    position: absolute;
    left: 75px;
    top: 132px;
    width: 1050px;
    height: 600px;
    background: var(--card-bg);
    box-shadow: 0 10px 30px rgba(0,0,0,0.18);
    overflow: hidden;
  }
  .card-art {
    position: absolute;
    left: 0;
    top: 0;
    width: 1050px;
    height: 600px;
  }
  .company-name {
    position: absolute;
    right: 95px;
    top: 62px;
    margin: 0;
    font-family: "Tinos", "Times New Roman", serif;
    font-weight: 700;
    font-size: 50px;
    color: var(--brand-red);
    letter-spacing: 0.5px;
  }
  .person {
    position: absolute;
    right: 80px;
    top: 196px;
    text-align: right;
    font-family: "Arimo", Arial, sans-serif;
  }
  .person-name {
    margin: 0;
    font-size: 31px;
    color: var(--accent-red);
    line-height: 1.1;
  }
  .person-role {
    margin: 2px 0 0;
    font-size: 21px;
    color: var(--ink);
  }
  .contacts {
    position: absolute;
    right: 40px;
    top: 310px;
    margin: 0;
    padding: 0;
    list-style: none;
    font-family: "Arimo", Arial, sans-serif;
    font-size: 23px;
    color: var(--ink);
  }
  .contact-item {
    display: flex;
    justify-content: flex-end;
    align-items: center;
    height: 46px;
  }
  .contact-icon {
    width: 22px;
    height: 22px;
    margin-left: 18px;
    fill: var(--accent-red);
  }
  .address {
    position: absolute;
    right: 40px;
    bottom: 34px;
    margin: 0;
    font-family: "Arimo", Arial, sans-serif;
    font-size: 23px;
    color: var(--ink);
  }
</style>
</head>
<body>
<article class="card">
  <svg class="card-art" viewBox="0 0 1050 600" aria-hidden="false">
    <defs>
      <linearGradient id="portraitTones" x1="0" y1="0" x2="1" y2="1">
        <stop offset="0" stop-color="var(--photo-warm)"/>
        <stop offset="0.45" stop-color="#6b4a3a"/>
        <stop offset="1" stop-color="var(--photo-dark)"/>
      </linearGradient>
    </defs>
    <path class="portrait-area" role="img" aria-label="Portrait photo of the managing director wearing a striped knit hat"
          d="M0,0 H390 C470,160 470,420 290,600 H0 Z" fill="url(#portraitTones)"/>
    <path class="curve-band" d="M398,0 H448 C520,180 500,430 318,600 H300 C480,420 478,160 398,0 Z" fill="var(--brand-red)"/>
  </svg>

  <h1 class="company-name">Quarry Lane Co.,Inc</h1>

  <div class="person">
    <p class="person-name">Employee Name</p>
    <p class="person-role">Managing Director</p>
  </div>

  <ul class="contacts">
    <li class="contact-item">(800) 555-0142
      <svg class="contact-icon" viewBox="0 0 24 24"><path d="M6.6 10.8a15 15 0 0 0 6.6 6.6l2.2-2.2c.3-.3.7-.4 1-.2 1.1.4 2.3.6 3.6.6.6 0 1 .4 1 1V20c0 .6-.4 1-1 1A17 17 0 0 1 3 4c0-.6.4-1 1-1h3.5c.6 0 1 .4 1 1 0 1.3.2 2.5.6 3.6.1.3 0 .7-.2 1z"/></svg>
    </li>
    <li class="contact-item">(480) 555-0187
      <svg class="contact-icon" viewBox="0 0 24 24"><path d="M6 2h12v5H6z M3 8h18a1 1 0 0 1 1 1v8h-4v5H6v-5H2V9a1 1 0 0 1 1-1z M8 15v5h8v-5z"/></svg>
    </li>
    <li class="contact-item">QLaneCo@mailbox.com
      <svg class="contact-icon" viewBox="0 0 24 24"><path d="M2 5h20v14H2z M3.5 6.5 12 13l8.5-6.5" stroke="#fff" stroke-width="1.5"/></svg>
    </li>
    <li class="contact-item">www.quarrylaneco.com
      <svg class="contact-icon" viewBox="0 0 24 24"><circle cx="12" cy="12" r="10"/><path d="M2 12h20 M12 2c3 3 3 17 0 20 M12 2c-3 3-3 17 0 20" stroke="#fff" stroke-width="1.3" fill="none"/></svg>
    </li>
  </ul>

  <p class="address">2145 W Harrow Way # B210-118 Tempe, Arizona</p>
</article>
</body>
</html>
```